Sleep/Snoring Business - Requires Website - Australia

We are seeking a simple to maintain website for our sleep business. The health care business provides diagnostic and treatment solutions for snoring, sleep disorders and other respiratory problems.

Ideally, colours to match the company logo (attached).

The page must be built using WORDPRESS.

Ideally site will have a home page outlining the business, with 5 sub pages - being "Diagnosis" "Treatment Options", "Prodcuts", "About Us", "Contact Us"

The site home page should include a large picture on the home page.

The "Treatment Options" and "Diagnosis" pages must include:
Allow for a few pictures with assocaited text, plus space for some embeded youtube videos.

"Prodcuts" page should have the ability to show 3-4 products across the page with text below.. that can include external URL to products

The "About Us" page must include:
1. a Map (google map) to identify the various locations. There are 6 in total.
2. A Section to describe our doctors/staff - allow for a picture and some text

The "Contact Us" page must include:
email form
telephone details

The overall design should have a clean and medical/safe feeling

Target Market(s)

People who snore and those with sleeping and respiratory disorders

Industry/Entity Type

Health Care

Coding

Coded - Design and coding required

Number of Pages Required

5+ page

Colors

Designer to choose colors to be used in the design.

Requirements
Must have
• The page must be built using WORDPRESS.
• Ideally site will have a home page outlining the business, with 5 sub pages - being "Diagnosis" "Treatment Options", "Prodcuts", "About Us", "Contact Us"
• The site home page should include a large picture on the home page.
• The "Treatment Options" and "Diagnosis" pages must include:
• Allow for a few pictures with assocaited text, plus space for some embeded youtube videos.
• "Prodcuts" page should have the ability to show 3-4 products across the page with text below.. that can include external URL to products
• The "About Us" page must include:
• 1. a Map (google map) to identify the various locations. There are 6 in total.
• 2. A Section to describe our doctors/staff - allow for a picture and some text
• The "Contact Us" page must include:
• email form
• telephone details
• Pictures must be licenced or free to use
Nice to have
• Home page pictures showing people sleeping well, snoring or fresh air (landscape) type transition pictures (at least 3).
Should not have
• Not to look cheap
• This is a high end healthcare business, so must look that way

```html
<!DOCTYPE html>
<html lang="en">
<head>
<meta charset="utf-8">
<title>Restwell — Home</title>
<link rel="stylesheet" href="https://fonts.googleapis.com/css2?family=Open+Sans:wght@400;600;700;800&display=swap">
<style>
  :root {
    --topbar: #464a5f;
    --topbar-text: #c3c6d0;
    --accent-yellow: #f7c844;
    --accent-red: #f0584c;
    --accent-purple: #5a5e93;
    --accent-teal: #8ed1c9;
    --ink: #3c3f55;
    --nav: #9a9db0;
    --white: #ffffff;
    --hero-light: #d3d8e5;
    --hero-mid: #c4cadb;
    --hero-dark: #aeb5cb;
  }
  * { box-sizing: border-box; margin: 0; padding: 0; }
  html, body { width: 1200px; height: 589px; overflow: hidden; }
  body { font-family: "Open Sans", sans-serif; background: var(--white); position: relative; }

  .topbar {
    height: 33px; background: var(--topbar);
    display: flex; align-items: center; justify-content: space-between;
    padding: 0 57px 0 80px;
    font-size: 11.5px; font-weight: 700; color: var(--topbar-text);
  }
  .contact-list, .account-links { display: flex; align-items: center; gap: 18px; }
  .contact-item { display: flex; align-items: center; gap: 6px; }
  .account-links .divider { width: 1px; height: 11px; background: #6a6e82; }
  .login { display: flex; align-items: center; gap: 8px; }

  .accent-strip { display: flex; height: 4px; }
  .accent-strip span { flex: 1; }
  .accent-strip .yellow { background: var(--accent-yellow); }
  .accent-strip .red { background: var(--accent-red); }
  .accent-strip .purple { background: var(--accent-purple); }
  .accent-strip .teal { background: var(--accent-teal); }

  .site-header {
    height: 70px; display: flex; align-items: center; justify-content: space-between;
    padding: 0 86px 0 80px; background: var(--white);
  }
  .brand { display: flex; align-items: center; gap: 6px; font-size: 23px; font-weight: 700; color: var(--ink); }
  .brand-dot { width: 16px; height: 16px; border-radius: 50%; background: var(--accent-red); }
  .main-nav { display: flex; align-items: center; gap: 17px; font-size: 12.5px; font-weight: 600; color: var(--nav); }
  .main-nav .current { color: var(--accent-red); }
  .main-nav .search { margin-left: 44px; display: flex; }

  .hero {
    position: absolute; top: 107px; left: 0; width: 1200px; height: 482px;
  }
  .hero-photo {
    position: absolute; inset: 0;
    background:
      radial-gradient(ellipse 260px 360px at 960px 300px, #eef0f6 0%, rgba(238,240,246,0) 70%),
      linear-gradient(90deg, var(--hero-light) 0%, var(--hero-mid) 60%, var(--hero-dark) 100%);
  }
  .hero-shade { position: absolute; top: 0; left: 0; width: 916px; height: 4px; background: #b9bcc6; }
  .hero-content { position: absolute; left: 80px; top: 92px; color: var(--white); }
  .hero-title { font-size: 86px; font-weight: 800; line-height: 78px; letter-spacing: 0.5px; }
  .hero-subtitle { margin-top: 12px; font-size: 21px; font-weight: 700; }
  .cta {
    margin-top: 48px; width: 238px; height: 58px; background: var(--accent-purple);
    display: flex; align-items: center; padding-left: 24px;
    font-size: 13px; font-weight: 700; color: var(--white);
  }
  .cta .cta-divider { width: 1px; height: 22px; background: rgba(255,255,255,0.35); margin: 0 16px 0 26px; }
</style>
</head>
<body>
  <div class="topbar">
    <div class="contact-list">
      <span class="contact-item">
        <svg width="10" height="10" viewBox="0 0 10 10"><path d="M2 0.5 L3.6 2.8 L2.6 3.8 Q3.6 6 6.2 7.4 L7.2 6.4 L9.5 8 L8.4 9.6 Q4 9.2 0.4 2 Z" fill="#c3c6d0"/></svg>
        (555) 018-2740
      </span>
      <span class="contact-item">
        <svg width="8" height="11" viewBox="0 0 8 11"><path d="M4 0 A4 4 0 0 1 8 4 Q8 6.5 4 11 Q0 6.5 0 4 A4 4 0 0 1 4 0 Z M4 2.3 A1.7 1.7 0 1 0 4 5.7 A1.7 1.7 0 1 0 4 2.3 Z" fill="#c3c6d0" fill-rule="evenodd"/></svg>
        48 Harbour Lane, Springfield 20145
      </span>
    </div>
    <div class="account-links">
      <span>Register</span>
      <span class="divider"></span>
      <span class="login">Login
        <svg width="15" height="14" viewBox="0 0 15 14" fill="none" stroke="#c3c6d0" stroke-width="1.4"><path d="M1 7 H9 M6 4 L9 7 L6 10"/><path d="M6 1 H14 V13 H6"/></svg>
      </span>
    </div>
  </div>
  <div class="accent-strip"><span class="yellow"></span><span class="red"></span><span class="purple"></span><span class="teal"></span></div>

  <header class="site-header">
    <div class="brand"><span class="brand-dot"></span>Restwell</div>
    <nav class="main-nav">
      <span class="current">Home</span>
      <span>Diagnosis</span>
      <span>Treatment Options</span>
      <span>Products</span>
      <span>About Us</span>
      <span>Contact Us</span>
      <span class="search">
        <svg width="14" height="14" viewBox="0 0 14 14" fill="none" stroke="#5a5e93" stroke-width="2"><circle cx="6" cy="6" r="4.5"/><path d="M9.3 9.3 L13 13"/></svg>
      </span>
    </nav>
  </header>

  <section class="hero">
    <div class="hero-photo" role="img" aria-label="Smiling doctor in a white coat with a stethoscope against a soft lavender backdrop"></div>
    <div class="hero-shade"></div>
    <div class="hero-content">
      <h1 class="hero-title">MORE THAN10,000<br>PEOPLE</h1>
      <p class="hero-subtitle">TRUSTED US WITH THEIR LIVES</p>
      <div class="cta">Make an Appointment
        <span class="cta-divider"></span>
        <svg width="22" height="22" viewBox="0 0 22 22" fill="none" stroke="#ffffff" stroke-width="1.4"><path d="M1 1 H21 V21 H1"/><path d="M4 11 H16 M13 8 L16 11 L13 14"/></svg>
      </div>
    </div>
  </section>
</body>
</html>
```